Property Development Business Cards

I need a business card design for Blue Harbour Developments Pty Ltd. We are a property development company in Australia and our name defines the five values that we adhere to, being Profitable, Partnerships, Quality Developments, Eco Friendly and Enduring Design.

I have attached the current logo that I use, it is just five yellow circles connected to a single cricle in the middle.

Target Market(s)

Our Target audience is real estate agents, owners of properties, builders and other trades

Industry/Entity Type

Business

Requirements
Must have
• Want to have two sides to the card, one with details and one to just highlight the company

```html
<!DOCTYPE html>
<html lang="en">
<head>
<meta charset="utf-8">
<title>Blue Harbour Developments – Business Cards</title>
<link rel="stylesheet" href="https://fonts.googleapis.com/css2?family=Arimo:wght@400;700&family=Cinzel:wght@700&display=swap">
<style>
  :root {
    --backdrop: #eeeae2;
    --card-white: #ffffff;
    --gold: #f1c000;
    --gold-deep: #e6a900;
    --ink: #1d1d1d;
    --ink-soft: #4a4a4a;
    --mark-orange: #f0a818;
  }
  * { margin: 0; padding: 0; box-sizing: border-box; }
  html, body { width: 1200px; height: 896px; overflow: hidden; }
  body {
    background: var(--backdrop);
    font-family: "Arimo", Arial, sans-serif;
    position: relative;
  }
  .card {
    position: absolute;
    top: 298px;
    width: 525px;
    height: 300px;
    box-shadow: 0 4px 14px rgba(0, 0, 0, 0.18);
    overflow: hidden;
  }
  .card--brand {
    left: 50px;
    background: linear-gradient(90deg,
      var(--gold) 0%, var(--gold) 6%, #f8dc6a 20%, var(--card-white) 36%,
      var(--card-white) 66%, #f9e07a 80%, var(--gold) 90%, var(--gold-deep) 100%);
  }
  .card--details {
    left: 625px;
    background: linear-gradient(90deg,
      var(--card-white) 0%, var(--card-white) 32%, #fbe9a0 50%,
      #f6d340 64%, var(--gold) 76%, var(--gold-deep) 100%);
  }
  .company-mark {
    position: absolute;
    display: flex;
    align-items: center;
    gap: 10px;
    color: var(--mark-orange);
    font-weight: 700;
    line-height: 1.15;
  }
  .company-mark__dot {
    flex: none;
    border-radius: 50%;
    background: var(--mark-orange);
  }
  .card--brand .company-mark {
    left: 170px; top: 70px; width: 210px;
    font-size: 20px;
  }
  .card--brand .company-mark__dot { width: 34px; height: 34px; }
  .website {
    position: absolute;
    left: 190px; bottom: 30px;
    font-size: 11px;
    color: var(--ink-soft);
    letter-spacing: 0.2px;
  }
  .card--details .company-mark {
    left: 28px; top: 108px; width: 160px;
    font-size: 14px;
  }
  .card--details .company-mark__dot { width: 26px; height: 26px; }
  .contact {
    position: absolute;
    left: 232px; top: 96px;
    color: var(--ink);
  }
  .contact__name {
    font-family: "Cinzel", "Times New Roman", serif;
    font-size: 22px;
    letter-spacing: 1.5px;
    margin-bottom: 4px;
  }
  .contact__role { font-size: 11px; margin-bottom: 6px; }
  .contact__line { font-size: 11px; line-height: 15px; }
</style>
</head>
<body>
  <section class="card card--brand" aria-label="Card front">
    <div class="company-mark">
      <span class="company-mark__dot"></span>
      <span class="company-mark__name">Blue Harbour Developments</span>
    </div>
    <p class="website">www.blueharbourdevelopments.com.au</p>
  </section>

  <section class="card card--details" aria-label="Card back">
    <div class="company-mark">
      <span class="company-mark__dot"></span>
      <span class="company-mark__name">Blue Harbour Developments</span>
    </div>
    <div class="contact">
      <h1 class="contact__name">Your Name</h1>
      <p class="contact__role">CEO</p>
      <p class="contact__line">Street Avenue 1234, Australia</p>
      <p class="contact__line">Phone : +0123456789</p>
      <p class="contact__line">Fax : +0123456789</p>
      <p class="contact__line">Email : mail@mail.com</p>
    </div>
  </section>
</body>
</html>
```